Fasteners Poly-bag design with KEVRA brand

We are trading with fasteners and rigging hardware and now we need a new design for a poly-bag. The header of poly-bag will contain two parts - top part (around 60%) will be static with our logo "KEVRA" and your type of design. The bottom part (around 40%) should be with different color for each group of fasteners or rigging hardware and with different text (5 groups in total). The border between the two part can be different from straight line (for example like wave or something else). I added a file with explanation and some samples of poly-bags. The total dimensions of the header are 80 mm/40 mm. The nylon part of poly-bag will have a background - I added a file with our image, but you can offer us different image also. Please when creating design, do it for full poly-bag, including the nylon part, not only header. The colors from header can continue to the nylon part also. I added a file "DESIGN SAMPLES" just as examples, what we expect to see. Of course you can offer your own variant of design! Thank you in advance!

Target Market(s)

Fasteners and rigging hardware

Industry/Entity Type

Fastener

Font styles to use
Other font styles liked:
• SAUCER BB - Logo Font

Colors

Designer to choose colors to be used in the design.

Requirements
Must have
• Our logo "KEVRA"

```html
<!DOCTYPE html>
<html lang="en">
<head>
<meta charset="utf-8">
<title>KEVRA fastener poly-bag headers</title>
<link rel="stylesheet" href="https://fonts.googleapis.com/css2?family=Roboto:wght@700&display=swap">
<style>
  :root {
    --page-bg: #ececec;
    --brand-red: #ec1c24;
    --strip-dark: #3d3d3d;
    --ink: #1c1c1c;
    --label-green: #39b54a;
    --label-orange: #f26522;
    --metal-light: #e4e4e4;
    --metal-mid: #b9b9b9;
    --metal-dark: #8f8f8f;
    --nylon-light: #fbfbfb;
    --nylon-shade: #e2e2e2;
  }
  * { margin: 0; padding: 0; box-sizing: border-box; }
  html, body {
    width: 1200px;
    height: 978px;
    overflow: hidden;
    background: var(--page-bg);
    font-family: "Roboto", Arial, sans-serif;
  }
  .canvas { position: relative; width: 1200px; height: 978px; }

  .bag {
    position: absolute;
    top: 166px;
    width: 390px;
    height: 646px;
    box-shadow: 0 3px 6px rgba(0,0,0,.18);
    background: var(--nylon-light);
  }
  .bag--hex { left: 181px; }
  .bag--lobe { left: 646px; }

  .bag__red-band {
    position: absolute; left: 0; top: 0; width: 63px; height: 100%;
    background: linear-gradient(to bottom, var(--brand-red) 0%, var(--brand-red) 40%, rgba(222,80,90,.85) 70%, rgba(236,28,36,0) 100%);
  }
  .bag__dark-strip {
    position: absolute; left: 63px; top: 0; width: 22px; height: 150px;
    background: var(--strip-dark);
  }
  .bag__icon-column {
    position: absolute; left: 63px; top: 196px; width: 22px; height: 450px;
    background: linear-gradient(to bottom, #3a3a3a 0%, #4a4a4a 70%, rgba(80,80,80,0) 100%);
  }
  .bag__metal {
    position: absolute; left: 85px; top: 0; width: 305px; height: 150px;
    background:
      linear-gradient(to right, rgba(255,255,255,0) 40%, rgba(255,255,255,.35) 100%),
      linear-gradient(to bottom, var(--metal-light), var(--metal-mid) 55%, var(--metal-dark));
  }
  .bag__hang-hole {
    position: absolute; left: 135px; top: 20px; width: 120px; height: 54px;
  }
  .bag__logo {
    position: absolute; left: 96px; top: 84px;
    font-weight: 700; font-size: 60px; line-height: 1;
    color: var(--ink); letter-spacing: 1px;
  }
  .bag__label {
    position: absolute; left: 0; top: 150px; width: 390px; height: 46px;
    display: flex; align-items: center; justify-content: center;
    font-weight: 700; font-size: 16px; color: var(--ink);
    letter-spacing: -0.2px; white-space: nowrap;
    box-shadow: 0 2px 3px rgba(0,0,0,.2);
  }
  .bag--hex .bag__label { background: var(--label-green); }
  .bag--lobe .bag__label { background: var(--label-orange); }

  .bag__nylon {
    position: absolute; left: 85px; top: 196px; width: 305px; height: 450px;
    background:
      radial-gradient(ellipse at 70% 35%, rgba(255,255,255,.9), rgba(255,255,255,0) 60%),
      linear-gradient(160deg, var(--nylon-light) 0%, var(--nylon-shade) 45%, #f2f2f2 70%, var(--nylon-shade) 100%);
  }
</style>
</head>
<body>
<main class="canvas">

  <section class="bag bag--hex">
    <div class="bag__red-band"></div>
    <div class="bag__dark-strip"></div>
    <div class="bag__metal" role="img" aria-label="Brushed metal panel with a pattern of silver squares"></div>
    <svg class="bag__hang-hole" viewBox="0 0 120 54" aria-hidden="true">
      <path fill="var(--page-bg)" d="M10 20 H42 A18 18 0 0 1 78 20 H110 A8 8 0 0 1 110 36 H10 A8 8 0 0 1 10 20 Z"/>
    </svg>
    <div class="bag__logo">KEVRA</div>
    <div class="bag__label">HEX BOLT FULL THREAD M6 X 6MM - STAINLESS</div>
    <div class="bag__icon-column" role="img" aria-label="Column of line drawings of washers, nuts, bolts and screws"></div>
    <div class="bag__nylon" role="img" aria-label="Clear nylon bag body"></div>
  </section>

  <section class="bag bag--lobe">
    <div class="bag__red-band"></div>
    <div class="bag__dark-strip"></div>
    <div class="bag__metal" role="img" aria-label="Brushed metal panel with a pattern of silver squares"></div>
    <svg class="bag__hang-hole" viewBox="0 0 120 54" aria-hidden="true">
      <path fill="var(--page-bg)" d="M10 20 H42 A18 18 0 0 1 78 20 H110 A8 8 0 0 1 110 36 H10 A8 8 0 0 1 10 20 Z"/>
    </svg>
    <div class="bag__logo">KEVRA</div>
    <div class="bag__label">LOBE CAP SCREW M5 X 6MM - STAINLESS</div>
    <div class="bag__icon-column" role="img" aria-label="Column of line drawings of washers, nuts, bolts and screws"></div>
    <div class="bag__nylon" role="img" aria-label="Clear nylon bag body"></div>
  </section>

</main>
</body>
</html>
```